Web App Connectivity

We are looking for a graphic that visually demonstrates the interconnectivy of various different web applications. We work with iPaaS platforms like Veltrix.com where we enable workflows across all the various web applications. We would like to graphically show this for a page on our website.

Businesses use a host of different web apps such as DealHarbor, LedgerPeak, Zorvan, Tellmark, Brisk Mailwise, Pallora, CareerLoom, and so on. We want to be able to show that Web apps can be connected for various tools such as CRM, Document Management, Markeing, ERP/Accounting, Sales, Legal and more to help drive productivity and efficiency by passing data and/or documents across these applications automatically.

```html
<!DOCTYPE html>
<html lang="en">
<head>
<meta charset="UTF-8">
<title>Web App Connectivity</title>
<link href="https://fonts.googleapis.com/css2?family=Montserrat:wght@600&display=swap" rel="stylesheet">
<style>
  :root {
    --bg-base: #26cc82;
    --bg-light: #62d996;
    --node-ring: #24b56e;
    --node-ring-line: #3cc784;
    --node-core: #5fd393;
    --hub-core: #27c97f;
    --hub-line: #52d897;
    --white: #ffffff;
    --tone-paper: #eef1ef;
    --tone-calendar: #f3e6e4;
    --tone-envelope: #f8dc95;
    --tone-folder: #fdcf1e;
  }
  html, body {
    margin: 0;
    padding: 0;
    width: 1200px;
    height: 865px;
    overflow: hidden;
  }
  .canvas {
    position: relative;
    width: 1200px;
    height: 865px;
    background:
      radial-gradient(ellipse 620px 520px at 820px 230px, var(--bg-light), transparent 75%),
      var(--bg-base);
    font-family: "Montserrat", sans-serif;
  }
  .diagram {
    position: absolute;
    inset: 0;
  }
  .app-visual {
    position: absolute;
    width: 56px;
    height: 50px;
    margin: -25px 0 0 -28px;
    border-radius: 6px;
  }
  .app-visual--cms { left: 287px; top: 264px; background: var(--tone-paper); }
  .app-visual--planner { left: 921px; top: 261px; background: var(--tone-calendar); }
  .app-visual--messaging { left: 286px; top: 575px; background: var(--tone-envelope); }
  .app-visual--storage { left: 913px; top: 577px; background: var(--tone-folder); }
  .label {
    position: absolute;
    transform: translateX(-50%);
    margin: 0;
    color: var(--white);
    font-size: 19px;
    font-weight: 600;
    line-height: 24px;
    letter-spacing: 0.2px;
    white-space: nowrap;
  }
  .label--cms { left: 263px; top: 378px; }
  .label--planner { left: 913px; top: 371px; }
  .label--messaging { left: 286px; top: 686px; }
  .label--storage { left: 930px; top: 698px; }
  .label--hub { left: 597px; top: 573px; }
</style>
</head>
<body>
<div class="canvas">
  <svg class="diagram" width="1200" height="865" viewBox="0 0 1200 865" aria-hidden="true">
    <defs>
      <filter id="soft-shadow" x="-40%" y="-40%" width="180%" height="180%">
        <feDropShadow dx="0" dy="4" stdDeviation="12" flood-color="#0d7a45" flood-opacity="0.28"/>
      </filter>
      <g id="node-ring">
        <circle r="90" fill="var(--node-ring)" filter="url(#soft-shadow)"/>
        <circle r="84" fill="none" stroke="var(--node-ring-line)" stroke-width="1"/>
        <circle r="78" fill="none" stroke="var(--white)" stroke-width="1.6" stroke-opacity="0.85"/>
        <circle r="52" fill="var(--node-core)"/>
      </g>
      <g id="plug">
        <rect x="-6" y="-9" width="12" height="18" rx="1.5" fill="var(--white)"/>
        <rect x="-12" y="-4" width="7" height="8" fill="var(--white)"/>
      </g>
    </defs>

    <g class="connectors" stroke="var(--white)" stroke-width="2" stroke-dasharray="6 5" fill="none">
      <line x1="366" y1="306" x2="466" y2="359"/>
      <line x1="838" y1="300" x2="730" y2="353"/>
      <line x1="366" y1="534" x2="466" y2="485"/>
      <line x1="832" y1="534" x2="730" y2="487"/>
    </g>
    <g class="plugs">
      <use href="#plug" transform="translate(475,363) rotate(28)"/>
      <use href="#plug" transform="translate(721,358) rotate(152)"/>
      <use href="#plug" transform="translate(475,480) rotate(-26)"/>
      <use href="#plug" transform="translate(721,482) rotate(-154)"/>
    </g>

    <g class="hub" transform="translate(598,422)">
      <circle r="128" fill="var(--hub-core)" filter="url(#soft-shadow)"/>
      <circle r="124" fill="none" stroke="var(--node-ring-line)" stroke-width="1.5"/>
      <circle r="112" fill="none" stroke="var(--hub-line)" stroke-width="1"/>
      <circle r="106" fill="none" stroke="var(--white)" stroke-width="1.8" stroke-opacity="0.85"/>
      <path class="hub-icon" d="M-30 22 A18 18 0 0 1 -28 -14 A26 26 0 0 1 20 -18 A20 20 0 0 1 30 22 Z"
            fill="none" stroke="var(--white)" stroke-width="3.2" stroke-linejoin="round"/>
    </g>

    <use href="#node-ring" x="287" y="264"/>
    <use href="#node-ring" x="921" y="261"/>
    <use href="#node-ring" x="286" y="575"/>
    <use href="#node-ring" x="913" y="577"/>
  </svg>

  <div class="app-visual app-visual--cms" role="img" aria-label="Content management app icon"></div>
  <div class="app-visual app-visual--planner" role="img" aria-label="Planner app calendar icon"></div>
  <div class="app-visual app-visual--messaging" role="img" aria-label="Messaging app mail icon"></div>
  <div class="app-visual app-visual--storage" role="img" aria-label="Cloud storage folder icon"></div>

  <p class="label label--cms">CMS APP</p>
  <p class="label label--planner">Planner APP</p>
  <p class="label label--messaging">Messaging APP</p>
  <p class="label label--storage">Storage APP</p>
  <p class="label label--hub">Routing Hub</p>
</div>
</body>
</html>
```